Meadow Reset sale graphics for social media

You MUST read the Brief in the WORD document and follow the instructions there. I want to create 10 social media graphics (new Instagram size 4:5 (1080 x 1350 pixels) focusing on our Mother’s Day Meadow Reset Sale graphics, using any of the pics attached. Use the attached pics, NO RANDOM STOCK PHOTOGRAPHY. For the color scheme of the graphics, they should all be complementary to the product colors or feel like Spring time.

Target Market(s)

primarily women

Requirements
Must have
• the photos and text attached

```html
<!DOCTYPE html>
<html lang="en">
<head>
<meta charset="utf-8">
<title>Meadow Reset Sale – Social Set</title>
<link href="https://fonts.googleapis.com/css2?family=Bebas+Neue&family=Great+Vibes&family=Playfair+Display:ital,wght@1,600&family=Yellowtail&display=swap" rel="stylesheet">
<style>
  :root{
    --board:#808080;
    --yellow:#f2c630;
    --white:#ffffff;
    --p1-bg:#d8e5fb; --p1-ink:#3a55a8; --p1-band:#3a5bb5; --p1-cyan:#27c4cf; --p1-badge:#c8117e;
    --p2-bg:#f9e2eb; --p2-ink:#561d86; --p2-band:#de79a7; --p2-edge:#b478a9;
    --p3-bg:#fde0e1; --p3-ink:#c04a7c; --p3-band:#c6232c; --p3-edge:#cfcfcf;
    --p4-bg:#d8eef5; --p4-ink:#4e6b7b; --p4-band:#4e6b7b; --p4-edge:#80adc2;
    --p5-bg:#e4e6ee; --p5-band:#23433a; --p5-edge:#9fcab6;
    --p6-bg:#c9d3fb; --p6-ink:#3b4fa4; --p6-band:#3d4fa6; --p6-edge:#9a6ccc;
    --p8-bg:#e6e8f1; --p8-band:#4f86e3; --p8-badge:#4a51a0;
    --p9-bg:#f6dbe8; --p9-ink:#c35a95; --p9-band:#c0609a; --p9-edge:#e7a9c8;
    --p10-bg:#eef7f1; --p10-ink:#5e8a75; --p10-band:#6b9a83; --p10-edge:#1f2e27;
  }
  *{box-sizing:border-box;margin:0;padding:0}
  html,body{width:1200px;height:1200px;overflow:hidden;background:var(--board)}
  .board{position:relative;width:1200px;height:1200px}
  .post{position:absolute;overflow:hidden}
  .post.large{width:295px;height:369px}
  .post.small{width:219px;height:273px}
  .post > *{position:absolute}
  .band{left:0;top:0;width:100%;height:100%}
  .headline{font-family:"Bebas Neue",sans-serif;line-height:.95;text-align:center;left:0;width:100%;white-space:nowrap;z-index:3}
  .script-sale{font-family:"Yellowtail","Great Vibes",cursive;color:var(--yellow);line-height:1;white-space:nowrap;z-index:4}
  .tagline{font-family:"Great Vibes",cursive;color:var(--white);text-align:center;line-height:1.15;z-index:3}
  .photo-person{border-radius:40% 40% 6px 6px;z-index:1}
  .photo-products{border-radius:6px;z-index:2}
  .badge{border-radius:50%;display:flex;flex-direction:column;align-items:center;justify-content:center;color:var(--white);font-family:"Bebas Neue",sans-serif;line-height:.85;z-index:3}
  .badge-row{display:flex;align-items:flex-start}
  .badge-num{line-height:.8}
  .badge-side{display:flex;flex-direction:column;line-height:.85}
</style>
</head>
<body>
<div class="board">

  <section class="post large" style="left:142px;top:68px;background:var(--p1-bg)">
    <svg class="band" viewBox="0 0 295 369"><path d="M0 0H42C22 40 10 80 0 112Z" fill="var(--p1-band)"/><path d="M295 140C250 255 140 330 0 348V369H295Z" fill="var(--p1-band)"/><path d="M295 120C255 230 170 300 60 330" stroke="#6b88d8" stroke-width="6" fill="none"/></svg>
    <div class="headline" style="top:18px;font-size:50px;color:var(--p1-ink)">Mother’s Day<br>Meadow Reset</div>
    <div class="photo-person" role="img" aria-label="Smiling woman in a white cropped sweater" style="left:38px;top:118px;width:110px;height:249px;background:linear-gradient(#3a2a26 0 30%,#f1eeee 30% 68%,#2a2a2e 68%)"></div>
    <div class="script-sale" style="left:150px;top:110px;font-size:62px;color:var(--p1-cyan)">Sale</div>
    <div class="badge" style="left:152px;top:176px;width:136px;height:136px;background:var(--p1-badge)">
      <div class="badge-row"><span class="badge-num" style="font-size:76px">25</span><span class="badge-side"><span style="font-size:40px">%</span><span style="font-size:29px">OFF</span></span></div>
      <span style="font-size:21px;margin-top:4px">EVERYTHING!</span>
    </div>
    <div class="photo-products" role="img" aria-label="Row of supplement bottles and serum tubes" style="left:5px;top:300px;width:175px;height:56px;background:linear-gradient(#ffffff,#e5e3ea)"></div>
  </section>

  <section class="post large" style="left:452px;top:68px;background:var(--p2-bg)">
    <svg class="band" viewBox="0 0 295 369"><path d="M0 0H30C15 60 6 120 0 170Z" fill="var(--p2-band)"/><path d="M295 120C230 205 120 230 62 290C35 320 22 350 16 369H295Z" fill="var(--p2-band)"/><path d="M295 120C230 205 120 230 62 290C35 320 22 350 16 369" stroke="var(--p2-edge)" stroke-width="8" fill="none"/></svg>
    <div class="headline" style="top:14px;font-size:50px;color:var(--p2-ink)">25% Off<br>Mother’s Day<br>Meadow Reset</div>
    <div class="script-sale" style="left:80px;top:162px;font-size:76px">Sale</div>
    <div class="photo-products" role="img" aria-label="Four supplement bottles" style="left:60px;top:256px;width:196px;height:106px;background:linear-gradient(#ffffff,#e6e3ec)"></div>
  </section>

  <section class="post large" style="left:763px;top:68px;background:var(--p3-bg)">
    <svg class="band" viewBox="0 0 295 369"><path d="M0 0H22C10 60 4 110 0 150Z" fill="var(--p3-edge)"/><path d="M295 128C240 232 120 250 62 300L40 369H295Z" fill="var(--p3-band)"/><path d="M295 128C240 232 120 250 62 300" stroke="var(--p3-edge)" stroke-width="8" fill="none"/></svg>
    <div class="headline" style="top:14px;font-size:50px;color:var(--p3-ink)">25% Off All<br>Supplements<br>Meadow Reset</div>
    <div class="script-sale" style="left:80px;top:162px;font-size:76px">Sale</div>
    <div class="photo-products" role="img" aria-label="Four supplement bottles" style="left:25px;top:258px;width:250px;height:102px;background:linear-gradient(#ffffff,#e6e3ec)"></div>
  </section>

  <section class="post large" style="left:142px;top:458px;background:var(--p4-bg)">
    <svg class="band" viewBox="0 0 295 369"><path d="M0 0H34C18 40 8 70 0 100Z" fill="var(--p4-band)"/><path d="M0 369V255C90 200 200 140 295 72V369Z" fill="var(--p4-band)"/><path d="M0 255C90 200 200 140 295 72" stroke="var(--p4-edge)" stroke-width="8" fill="none"/></svg>
    <div class="headline" style="top:14px;font-size:50px;color:var(--p4-ink)">25% Off<br>Meadow Reset</div>
    <div class="photo-person" role="img" aria-label="Close portrait of a smiling woman" style="left:0;top:118px;width:97px;height:251px;background:linear-gradient(#2f2422 0 25%,#8a5e4a 25% 65%,#f0eeee 65%)"></div>
    <div class="script-sale" style="left:120px;top:112px;font-size:74px">Sale</div>
    <div style="left:98px;top:198px;width:197px;height:54px;background:var(--p4-band);border-radius:8px 0 0 0;font-family:'Playfair Display',serif;font-style:italic;font-weight:600;color:var(--yellow);font-size:20px;line-height:1.1;text-align:center;padding-top:4px;z-index:3">Spring Reset.<br>Summer Ready</div>
    <div class="photo-products" role="img" aria-label="Four supplement bottles with spring flowers" style="left:98px;top:264px;width:197px;height:100px;background:linear-gradient(#ffffff,#e4e6ec)"></div>
  </section>

  <section class="post large" style="left:452px;top:458px;background:var(--p5-bg)">
    <svg class="band" viewBox="0 0 295 369"><path d="M0 0H34C18 40 8 70 0 100Z" fill="var(--p5-band)"/><path d="M295 150C230 190 150 215 0 330V369H295Z" fill="var(--p5-band)"/><path d="M295 150C230 190 150 215 0 330" stroke="var(--p5-edge)" stroke-width="8" fill="none"/><path d="M285 130C270 170 240 190 200 205" stroke="var(--yellow)" stroke-width="8" fill="none"/></svg>
    <div class="photo-person" role="img" aria-label="Smiling woman in a white cropped sweater" style="left:36px;top:9px;width:100px;height:200px;background:linear-gradient(#3a2a26 0 28%,#f1eeee 28% 72%,#2a2a2e 72%)"></div>
    <div class="badge" style="left:122px;top:10px;width:164px;height:164px;background:var(--p5-band)">
      <div class="badge-row"><span class="badge-num" style="font-size:92px">25</span><span class="badge-side"><span style="font-size:50px">%</span><span style="font-size:35px">OFF</span></span></div>
      <span style="font-size:26px;margin-top:4px">EVERYTHING!</span>
    </div>
    <div class="photo-products" role="img" aria-label="Row of supplement bottles and serum tubes" style="left:5px;top:166px;width:150px;height:50px;background:linear-gradient(#ffffff,#e5e3ea)"></div>
    <div class="headline" style="left:105px;width:180px;top:212px;font-size:37px;color:var(--white)">Mother’s Day<br>Meadow Reset</div>
    <div class="script-sale" style="left:122px;top:288px;font-size:64px">Sale</div>
  </section>

  <section class="post large" style="left:763px;top:458px;background:var(--p6-bg)">
    <svg class="band" viewBox="0 0 295 369"><path d="M0 0H34C18 40 8 70 0 100Z" fill="var(--p6-band)"/><path d="M295 100C230 200 130 250 0 262V369H295Z" fill="var(--p6-band)"/><path d="M295 100C230 200 130 250 0 262" stroke="var(--p6-edge)" stroke-width="10" fill="none"/></svg>
    <div class="headline" style="top:14px;font-size:50px;color:var(--p6-ink)">25% Off<br>Mother’s Day</div>
    <div class="photo-person" role="img" aria-label="Smiling woman in a white sweater" style="left:25px;top:116px;width:110px;height:140px;background:linear-gradient(#3a2a26 0 35%,#f1eeee 35%)"></div>
    <div class="script-sale" style="left:130px;top:110px;font-size:68px">Sale</div>
    <div class="tagline" style="left:138px;top:186px;width:150px;font-size:25px">Feel Amazing<br>Again!</div>
    <div class="photo-products" role="img" aria-label="Four supplement bottles" style="left:25px;top:258px;width:240px;height:98px;background:linear-gradient(#ffffff,#e6e3ec)"></div>
  </section>

  <section class="post small" style="left:142px;top:840px;background:var(--p4-bg)">
    <svg class="band" viewBox="0 0 219 273"><path d="M0 0H26C14 30 6 55 0 78Z" fill="var(--p4-band)"/><path d="M219 80C170 160 100 205 20 273H219Z" fill="var(--p4-band)"/><path d="M219 80C170 160 100 205 20 273" stroke="var(--p4-edge)" stroke-width="6" fill="none"/></svg>
    <div class="headline" style="top:12px;font-size:38px;color:var(--p4-ink)">25% Off<br>Meadow Reset</div>
    <div class="script-sale" style="left:55px;top:90px;font-size:54px">Sale</div>
    <div class="photo-products" role="img" aria-label="Four supplement bottles with spring flowers" style="left:35px;top:164px;width:180px;height:106px;background:linear-gradient(#ffffff,#e4e6ec)"></div>
  </section>

  <section class="post small" style="left:373px;top:840px;background:var(--p8-bg)">
    <svg class="band" viewBox="0 0 219 273"><path d="M0 0H26C14 30 6 55 0 78Z" fill="var(--p8-band)"/><path d="M219 50C180 120 130 180 82 273H219Z" fill="var(--p8-band)"/><path d="M219 50C180 120 130 180 82 273" stroke="#e57aa8" stroke-width="6" fill="none"/></svg>
    <div class="photo-person" role="img" aria-label="Smiling woman in a white cropped sweater" style="left:20px;top:92px;width:80px;height:150px;background:linear-gradient(#3a2a26 0 30%,#f1eeee 30% 72%,#2a2a2e 72%)"></div>
    <div class="badge" style="left:78px;top:6px;width:130px;height:130px;background:var(--p8-badge)">
      <div class="badge-row"><span class="badge-num" style="font-size:70px">25</span><span class="badge-side"><span style="font-size:38px">%</span><span style="font-size:27px">OFF</span></span></div>
      <span style="font-size:18px;margin-top:2px">MOTHER’S DAY</span>
    </div>
    <div class="script-sale" style="left:110px;top:136px;font-size:44px">Sale</div>
    <div class="photo-products" role="img" aria-label="Row of supplement bottles and serum tubes" style="left:5px;top:226px;width:112px;height:32px;background:linear-gradient(#ffffff,#e5e3ea)"></div>
    <div class="headline" style="left:120px;width:98px;top:186px;font-size:16px;line-height:1.1;color:var(--white)">Detox this<br>spring.<br><span style="color:var(--yellow)">Shine*</span><br><span style="color:var(--yellow)">this summer</span></div>
  </section>

  <section class="post small" style="left:603px;top:840px;background:var(--p9-bg)">
    <svg class="band" viewBox="0 0 219 273"><path d="M0 0H26C14 30 6 55 0 78Z" fill="var(--p9-band)"/><path d="M219 60C170 130 100 165 0 205V273H219Z" fill="var(--p9-band)"/><path d="M219 60C170 130 100 165 0 205" stroke="var(--p9-edge)" stroke-width="6" fill="none"/></svg>
    <div class="headline" style="top:12px;font-size:38px;color:var(--p9-ink)">25% Off<br>Mother’s Day</div>
    <div class="photo-person" role="img" aria-label="Smiling woman in a white sweater" style="left:10px;top:92px;width:92px;height:181px;background:linear-gradient(#3a2a26 0 30%,#f1eeee 30%)"></div>
    <div class="script-sale" style="left:95px;top:88px;font-size:52px">Sale</div>
    <div class="tagline" style="left:108px;top:146px;width:100px;font-size:20px">Refresh<br>Your Body</div>
    <div class="photo-products" role="img" aria-label="Four supplement bottles" style="left:35px;top:198px;width:142px;height:72px;background:linear-gradient(#ffffff,#e6e3ec)"></div>
  </section>

  <section class="post small" style="left:835px;top:840px;background:var(--p10-bg)">
    <svg class="band" viewBox="0 0 219 273"><path d="M0 0H26C14 30 6 55 0 78Z" fill="var(--p10-band)"/><path d="M219 70C175 140 100 190 0 245V273H219Z" fill="var(--p10-band)"/><path d="M219 70C175 140 100 190 0 245" stroke="var(--p10-edge)" stroke-width="6" fill="none"/></svg>
    <div class="headline" style="top:12px;font-size:38px;color:var(--p10-ink)">25% Off<br>Mother’s Day</div>
    <div class="photo-person" role="img" aria-label="Smiling woman in a white cropped sweater" style="left:30px;top:92px;width:88px;height:140px;background:linear-gradient(#3a2a26 0 30%,#f1eeee 30% 75%,#2a2a2e 75%)"></div>
    <div class="script-sale" style="left:100px;top:88px;font-size:52px">Sale</div>
    <div class="tagline" style="left:120px;top:146px;width:97px;font-size:15px;line-height:1.3">Meadow<br>Reset for a<br>Summer<br>Body</div>
    <div class="photo-products" role="img" aria-label="Row of supplement bottles and serum tubes with flowers" style="left:10px;top:230px;width:205px;height:40px;background:linear-gradient(#ffffff,#e5e3ea)"></div>
  </section>

</div>
</body>
</html>
```